Business Card Design Project

We need a business card design for a management consultancy focused on financial innovation and digital money, run by experts from the Financial Services, Telecoms and Money Transfer industries.
Our products include services such as Mobile Payments, Mobile Money, Digital Wallets, Online Payments, Branchless Banking and more. We work with regulatory information, business plans, financial modelling, strategic planning, new products functional specification, new technologies evaluation, etc.
See company logo attached.
We would like to see 2 versions: one in portuguese and one in english (regarding data information). You can see below information needed (whenever there is a difference between the two versions, the first one is in english and the second one in portuguese).

Name
Position
Phone/ Tel: ++55-11-xxxx-xxxx
Cell/ Cel: ++55-11-9 xxxx-xxxx
Dr. Tavares Lobato Av., 318 - Tower II - 16th floor / Avenida Dr. Tavares Lobato, 318 - Torre II - 16o. andar
São Paulo - SP
01327-118 - Brazil/ 01327-118 - Brasil

Target Market(s)

Audience: C-level executives from banks, credit card companies, acquirers, IT developers, retailers

Industry/Entity Type

Financial

Requirements
Must have
• Must use the logo and information above. Front must have white background. Back side should have only logo.
Nice to have
• Back should be in another colour but if it seems too exxagerated, maintain back in white also.
Should not have
• Do not add other illustrations to the business card.

```html
<!DOCTYPE html>
<html lang="pt-BR">
<head>
<meta charset="utf-8">
<title>M Ferreira – Business Cards</title>
<link href="https://fonts.googleapis.com/css2?family=Cinzel:wght@400;500&family=Open+Sans:wght@400&display=swap" rel="stylesheet">
<style>
  :root {
    --bg: #e9e9ea;
    --card: #ffffff;
    --navy: #1f2f7a;
    --blue: #2a3f9e;
    --blue-dark: #0f1a52;
    --ink: #2b2b2b;
    --black: #1c1c1e;
  }
  * { margin: 0; padding: 0; box-sizing: border-box; }
  html, body { width: 1200px; height: 675px; overflow: hidden; }
  body {
    background: var(--bg);
    display: flex;
    align-items: center;
    justify-content: center;
    gap: 48px;
  }
  .card {
    position: relative;
    width: 540px;
    height: 309px;
    background: var(--card);
    box-shadow: 0 2px 10px rgba(0,0,0,.12);
    overflow: hidden;
  }
  .brand {
    position: absolute;
    left: 40px;
    top: 72px;
    display: flex;
    align-items: flex-end;
    gap: 10px;
  }
  .brand-square {
    width: 40px;
    height: 40px;
    background: var(--navy);
  }
  .brand-text { line-height: 1; white-space: nowrap; }
  .brand-name {
    font-family: "Cinzel", serif;
    font-weight: 400;
    font-size: 30px;
    color: var(--navy);
  }
  .brand-tagline {
    font-family: "Cinzel", serif;
    font-weight: 400;
    font-size: 12.5px;
    color: var(--navy);
    margin-top: 3px;
  }
  .person {
    position: absolute;
    left: 74px;
    top: 170px;
    text-align: right;
  }
  .person-name {
    font-family: "Cinzel", serif;
    font-size: 17px;
    color: var(--navy);
  }
  .person-role {
    font-family: "Open Sans", sans-serif;
    font-size: 10px;
    color: var(--ink);
    margin-top: 1px;
  }
  .contact {
    position: absolute;
    left: 300px;
    top: 134px;
    list-style: none;
    font-family: "Open Sans", sans-serif;
    font-size: 10.5px;
    line-height: 15px;
    color: var(--ink);
    white-space: nowrap;
  }
  .contact li { display: flex; align-items: flex-start; gap: 6px; }
  .contact .icon { width: 10px; height: 10px; margin-top: 2px; flex: none; fill: var(--navy); }
  .contact .indent { padding-left: 16px; }
  .bands { position: absolute; left: 0; bottom: 0; width: 540px; height: 40px; }
</style>
</head>
<body>

<svg width="0" height="0" style="position:absolute">
  <defs>
    <linearGradient id="band-blue" x1="0" y1="0" x2="0" y2="1">
      <stop offset="0" stop-color="#3349b0"/>
      <stop offset="1" stop-color="#0f1a52"/>
    </linearGradient>
    <symbol id="icon-phone" viewBox="0 0 10 10"><path d="M1 2.5C1 1.5 2 1 5 1s4 .5 4 1.5V4H7V3H3v1H1zM2 5h6l1 4H1z"/></symbol>
    <symbol id="icon-mobile" viewBox="0 0 10 10"><path d="M2.5 0h5a1 1 0 0 1 1 1v8a1 1 0 0 1-1 1h-5a1 1 0 0 1-1-1V1a1 1 0 0 1 1-1zM3 1.5v6h4v-6zM5 8.2a.6.6 0 1 0 0 1.2.6.6 0 0 0 0-1.2z"/></symbol>
    <symbol id="icon-pin" viewBox="0 0 10 10"><path d="M5 0a3.5 3.5 0 0 1 3.5 3.5C8.5 6 5 10 5 10S1.5 6 1.5 3.5A3.5 3.5 0 0 1 5 0zm0 2a1.4 1.4 0 1 0 0 2.8A1.4 1.4 0 0 0 5 2z"/></symbol>
  </defs>
</svg>

<section class="card card-pt">
  <div class="brand">
    <div class="brand-square"></div>
    <div class="brand-text">
      <div class="brand-name">M Ferreira</div>
      <div class="brand-tagline">Consultoria Estratégica</div>
    </div>
  </div>
  <div class="person">
    <div class="person-name">Your Long Name</div>
    <div class="person-role">Director</div>
  </div>
  <ul class="contact">
    <li><svg class="icon"><use href="#icon-phone"/></svg>++55-11-xxxx-xxxx</li>
    <li><svg class="icon"><use href="#icon-mobile"/></svg>++55-11-9 xxxx-xxxx</li>
    <li><svg class="icon"><use href="#icon-pin"/></svg>Dr. Tavares Lobato, 318 - Torre II -</li>
    <li class="indent">16o. andar São Paulo - SP</li>
    <li class="indent">01327-118 - Brazil</li>
  </ul>
  <svg class="bands" viewBox="0 0 540 40">
    <polygon points="318,8 540,8 540,24 318,24" fill="var(--black)"/>
    <polygon points="0,24 300,24 318,14 332,14 332,40 0,40" fill="url(#band-blue)"/>
    <rect x="332" y="24" width="208" height="16" fill="var(--card)"/>
  </svg>
</section>

<section class="card card-en">
  <div class="brand">
    <div class="brand-square"></div>
    <div class="brand-text">
      <div class="brand-name">M Ferreira</div>
      <div class="brand-tagline">Management Consulting</div>
    </div>
  </div>
  <div class="person">
    <div class="person-name">Your Long Name</div>
    <div class="person-role">Director</div>
  </div>
  <ul class="contact">
    <li><svg class="icon"><use href="#icon-phone"/></svg>++55-11-xxxx-xxxx</li>
    <li><svg class="icon"><use href="#icon-mobile"/></svg>++55-11-9 xxxx-xxxx</li>
    <li><svg class="icon"><use href="#icon-pin"/></svg>Dr. Tavares Lobato Av., 318 - Tower II</li>
    <li class="indent">16th floor / Avenida</li>
    <li class="indent">01327-118 - Brazil</li>
  </ul>
  <svg class="bands" viewBox="0 0 540 40">
    <polygon points="318,8 540,8 540,24 318,24" fill="var(--black)"/>
    <polygon points="0,24 300,24 318,14 332,14 332,40 0,40" fill="url(#band-blue)"/>
    <rect x="332" y="24" width="208" height="16" fill="var(--card)"/>
  </svg>
</section>

</body>
</html>
```